I'm looking to get the bottom (underneath the window) of the attached ticket booth wrapped with a modern design. The Dimensions of the final print is 68.5" wide x 37.5" tall, plus applicable safety margins. I'm open for pretty much any idea.

Key words are:

1.) "CAPTURE YOUR EXPERIENCE WITH A MEMORABLE PHOTO"

Follow us at:
IG: @skymorrow_
FB: @my.skyMORROW

2.) Our slogan should be mentioned as well "The GRANDEST ROTOR Journey" and "Leap INTO Bold Horizons"

3.) Also, a mention of "COLD DRINKS" as well, since we sell cold beverages during each event too.

Not all of the attached pictures have to be used. I just wanted to provide as many as possible for you guys to choose from. I have attached 3 pictures of the ticket booth as well, so you get an idea of how the space underneath the window is going to look.

Target Market(s)

Aviation, General Public, Adventure

Industry/Entity Type

Aviation

Colors
0054AA
0677BA
7BADD7
CADEEF
E8F1F8

Requirements
Must have
• Our Slogan, and the 3 key facts referenced in the project description

```html
<!DOCTYPE html>
<html lang="en">
<head>
<meta charset="utf-8">
<title>skyMORROW Booth Wrap</title>
<link rel="stylesheet" href="https://fonts.googleapis.com/css2?family=Poppins:ital,wght@0,600;0,800;0,900;1,800;1,900&display=swap">
<style>
  :root {
    --brand-deep: #0054AA;
    --brand-mid: #0677BA;
    --brand-soft: #7BADD7;
    --brand-pale: #CADEEF;
    --brand-mist: #E8F1F8;
    --ink: #111111;
    --paper: #ffffff;
    --accent-gold: #F5A623;
    --stage: #e9edf1;
  }
  * { box-sizing: border-box; margin: 0; padding: 0; }
  html, body { width: 1200px; height: 900px; overflow: hidden; }
  body {
    background: var(--stage);
    font-family: "Poppins", sans-serif;
    display: flex; align-items: center; justify-content: center;
  }
  .wrap-panel {
    position: relative;
    width: 1100px; height: 602px;
    background: var(--paper);
    overflow: hidden;
    box-shadow: 0 8px 30px rgba(0,0,0,.18);
  }
  .wrap-art { position: absolute; inset: 0; }
  .headline {
    position: absolute; left: 48px; top: 30px;
    color: var(--ink); font-weight: 900; line-height: 1.02;
    text-transform: uppercase;
  }
  .headline span { display: block; }
  .headline .h-sm { font-size: 38px; }
  .headline .h-xl { font-size: 58px; letter-spacing: -1px; }
  .headline .h-md { font-size: 36px; }
  .headline .h-lg { font-size: 52px; letter-spacing: -1px; }
  .slogan-box {
    position: absolute; left: 0; top: 318px; width: 372px; height: 108px;
    background: var(--brand-deep); color: var(--paper);
    padding: 8px 0 0 48px; line-height: 1.02; font-weight: 800;
  }
  .slogan-box .s-small { font-size: 26px; }
  .slogan-box .s-big { font-size: 36px; text-transform: uppercase; display: block; }
  .slogan-box .s-tail { font-size: 26px; }
  .tagline {
    position: absolute; left: 48px; top: 436px;
    color: var(--ink); font-weight: 800; font-style: italic; line-height: 1.05;
  }
  .tagline .t-lead { font-size: 26px; }
  .tagline .t-strong { font-size: 36px; font-weight: 900; }
  .tagline .t-line { font-size: 26px; display: block; }
  .cold-drinks {
    position: absolute; left: 42px; top: 548px;
    color: var(--paper); font-size: 26px; font-weight: 900; font-style: italic;
    letter-spacing: .5px;
  }
  .brand-mark {
    position: absolute; left: 470px; top: 145px; width: 180px; height: 180px;
    display: flex; align-items: center; justify-content: center;
    color: var(--paper); font-size: 24px; font-weight: 800;
  }
  .follow {
    position: absolute; left: 866px; top: 500px; line-height: 1.45;
  }
  .follow .f-title { color: var(--accent-gold); font-size: 19px; font-weight: 600; }
  .follow .f-handle { color: var(--paper); font-size: 17px; font-weight: 600; display: flex; align-items: center; gap: 8px; }
  .follow .f-dot { width: 9px; height: 9px; border-radius: 50%; background: var(--paper); }
</style>
</head>
<body>
  <main class="wrap-panel">
    <svg class="wrap-art" width="1100" height="602" viewBox="0 0 1100 602">
      <defs>
        <linearGradient id="skyline-tint" x1="0" y1="0" x2="1" y2="1">
          <stop offset="0" stop-color="#0677BA"/>
          <stop offset="1" stop-color="#0054AA"/>
        </linearGradient>
        <linearGradient id="cockpit-tones" x1="0" y1="0" x2="1" y2="1">
          <stop offset="0" stop-color="#CADEEF"/>
          <stop offset=".55" stop-color="#7b8894"/>
          <stop offset="1" stop-color="#2c3138"/>
        </linearGradient>
        <linearGradient id="aerial-grey" x1="0" y1="0" x2="0" y2="1">
          <stop offset="0" stop-color="#c9ccd0"/>
          <stop offset="1" stop-color="#4b4f55"/>
        </linearGradient>
        <linearGradient id="drink-amber" x1="0" y1="0" x2="0" y2="1">
          <stop offset="0" stop-color="#f0a04a"/>
          <stop offset="1" stop-color="#b8460c"/>
        </linearGradient>
      </defs>

      <path class="sky-band" role="img" aria-label="Aerial city view tinted in brand blue"
            d="M420 0 H1100 V330 C1000 120 820 60 640 110 C560 130 490 160 440 40 Z"
            fill="url(#skyline-tint)"/>

      <path class="cockpit-photo" role="img" aria-label="Photo of a pilot at the controls flying over a city"
            d="M600 350 C640 180 760 70 900 58 C980 52 1050 70 1100 100 V470 C1000 440 900 470 820 520 Z"
            fill="url(#cockpit-tones)" stroke="#ffffff" stroke-width="10"/>

      <path class="aerial-photo" role="img" aria-label="Photo of a tour helicopter flying above the waterfront"
            d="M400 602 V410 C470 370 540 360 610 350 L820 520 C780 560 750 585 740 602 Z"
            fill="url(#aerial-grey)" stroke="#ffffff" stroke-width="10"/>

      <path class="follow-field" d="M780 602 C820 520 900 480 1000 470 C1040 468 1075 474 1100 480 V602 Z"
            fill="var(--brand-deep)" stroke="#ffffff" stroke-width="8"/>

      <circle class="mark-disc" cx="560" cy="235" r="104" fill="#ffffff"/>
      <circle cx="560" cy="235" r="96" fill="var(--ink)"/>

      <path class="drinks-wave" d="M0 545 C140 535 280 530 400 500 V602 H0 Z" fill="var(--ink)"/>

      <rect class="drinks-art" role="img" aria-label="Two cold amber drinks in glasses"
            x="300" y="500" width="78" height="86" rx="6" fill="url(#drink-amber)"/>
    </svg>

    <h1 class="headline">
      <span class="h-sm">Capture your</span>
      <span class="h-xl">Experience</span>
      <span class="h-md">With a</span>
      <span class="h-lg">Memorable</span>
      <span class="h-md">Photo</span>
    </h1>

    <div class="slogan-box">
      <span class="s-small">The </span><span class="s-small">GRANDEST</span>
      <span class="s-big">Rotor</span>
      <span class="s-tail">Journey</span>
    </div>

    <p class="tagline">
      <span class="t-lead">Leap </span><span class="t-strong">INTO</span>
      <span class="t-line">Bold Horizons</span>
    </p>

    <p class="cold-drinks">COLD DRINKS</p>

    <div class="brand-mark">skyMORROW</div>

    <div class="follow">
      <p class="f-title">Follow us at:</p>
      <p class="f-handle"><span class="f-dot"></span>@skymorrow_</p>
      <p class="f-handle"><span class="f-dot"></span>@my.skyMORROW</p>
    </div>
  </main>
</body>
</html>
```